PPT Template for an investment fund to use in their pitchbooks

Our firm is an international investment fund and are seeking a PPT template to use in our pitch book (and subsequent PPTs). We would need a template for a title slide and then subsequent text/info slides. A clean & uncluttered feel is preferred as well as no watermark on slides. Please see our logo attached. The logo color code is #19478d. Font is Gotham-Medium.

Target Market(s)

Sophisticated investors

Industry/Entity Type

Finance

Colors
ffffff
0356a4

```html
<!DOCTYPE html>
<html lang="en">
<head>
<meta charset="utf-8">
<title>Pangolin Capital Partners – Pitchbook Template Overview</title>
<link href="https://fonts.googleapis.com/css2?family=Montserrat:wght@600;800&family=Poppins:wght@300;400;600&display=swap" rel="stylesheet">
<style>
:root{
  --frame:#0c3a5a;
  --navy:#121a61;
  --ink:#111318;
  --blue:#0356a4;
  --sky:#3fc0d8;
  --lav:#8b8fd8;
  --lav-dark:#6c70c4;
  --slate:#56688a;
  --muted:#5a5f6e;
  --white:#ffffff;
  --rule:#e3e5ee;
}
*{margin:0;padding:0;box-sizing:border-box}
html,body{width:1200px;height:1200px;overflow:hidden;background:var(--frame)}
body{position:relative;font-family:"Poppins",sans-serif;color:var(--ink)}
.slide{position:absolute;width:285px;height:220px;background:var(--white);overflow:hidden}
.slide *{position:absolute}
.col1{left:0}.col2{left:305px}.col3{left:610px}.col4{left:915px}
.row1{top:19px}.row2{top:252px}.row3{top:488px}.row4{top:724px}.row5{top:960px}
.heading{font-family:"Montserrat",sans-serif;font-weight:800;font-size:14px;line-height:1.15;color:var(--ink);white-space:nowrap}
.heading.barred{padding-left:7px}
.heading.barred::before{content:"";position:absolute;left:0;top:1px;width:1px;height:15px;background:var(--ink)}
.lorem{font-size:3.2px;line-height:1.6;color:var(--muted)}
.label{font-family:"Montserrat",sans-serif;font-weight:600;font-size:4.4px;color:var(--navy);white-space:nowrap}
.art{background:linear-gradient(160deg,#9ea2e4,var(--lav-dark))}
.photo-city{background:linear-gradient(180deg,#2d6fbf 0%,#1a3f86 55%,#0b1f4f 100%)}
.photo-light{background:linear-gradient(160deg,#d7e3f1,#6d92c3)}
.pill-v{width:14px;border-radius:7px;background:var(--navy);display:flex;align-items:center;justify-content:center}
.pill-v span{position:static;writing-mode:vertical-rl;transform:rotate(180deg);font-family:"Montserrat",sans-serif;font-weight:600;font-size:4px;color:var(--white);white-space:nowrap}
.vlabel{writing-mode:vertical-rl;transform:rotate(180deg);font-family:"Montserrat",sans-serif;font-weight:600;font-size:4px;color:var(--ink);white-space:nowrap}
.pill-h{height:14px;border-radius:7px;background:var(--navy);color:var(--white);font-family:"Montserrat",sans-serif;font-weight:600;font-size:4.4px;display:flex;align-items:center;justify-content:center}
.bullet{padding-left:6px}
.bullet::before{content:"";position:absolute;left:0;top:1.5px;width:2.5px;height:2.5px;border-radius:50%;background:var(--navy)}
.year{font-size:7.5px;color:var(--ink)}
.num{font-size:13px;color:var(--navy)}
svg{overflow:visible}
</style>
</head>
<body>

<!-- Row 1 -->
<section class="slide col1 row1">
  <div style="left:14px;top:42px;width:257px;height:135px;background:var(--slate)"></div>
  <h1 class="heading" style="left:34px;top:81px;color:var(--white);font-size:13.5px;line-height:1.3">Welcome To Our<br>Company</h1>
  <p class="lorem" style="left:34px;top:119px;width:140px;color:#d8deea">Pangolin Capital Partners invests with long term partners across global markets, seeking durable value and disciplined growth for every client portfolio we manage together.</p>
</section>

<section class="slide col2 row1">
  <div style="left:26px;top:73px;width:42px;height:1px;background:var(--ink)"></div>
  <h2 class="heading" style="left:26px;top:79px;font-size:13px">Table Of<br>Contents</h2>
  <div style="left:26px;top:118px;width:42px;height:1px;background:var(--ink)"></div>
  <div style="left:128px;top:51px;width:160px;height:140px">
    <div style="left:0;top:0;width:14px;height:14px;border:1px solid var(--navy);border-radius:50%;font-size:3.6px;display:flex;align-items:center;justify-content:center;color:var(--navy)"><span style="position:static">01</span></div>
    <p class="label" style="left:22px;top:0">Introduction</p>
    <p class="lorem" style="left:22px;top:5px;width:112px">Overview of the firm, our approach and the markets we serve across regions.</p>
    <div style="left:0;top:26px;width:14px;height:14px;border:1px solid var(--navy);border-radius:50%;font-size:3.6px;display:flex;align-items:center;justify-content:center;color:var(--navy)"><span style="position:static">02</span></div>
    <p class="label" style="left:22px;top:26px">About Us</p>
    <p class="lorem" style="left:22px;top:31px;width:112px">Our team, our structure and the values that guide every investment decision.</p>
    <div style="left:0;top:53px;width:14px;height:14px;border:1px solid var(--blue);border-radius:50%;font-size:3.6px;display:flex;align-items:center;justify-content:center;color:var(--blue)"><span style="position:static">03</span></div>
    <p class="label" style="left:22px;top:53px;color:var(--blue)">Company Mission &amp; History</p>
    <p class="lorem" style="left:22px;top:58px;width:112px">How the fund began and where we intend to take it over the coming decade.</p>
    <div style="left:0;top:80px;width:14px;height:14px;border:1px solid var(--sky);border-radius:50%;font-size:3.6px;display:flex;align-items:center;justify-content:center;color:var(--sky)"><span style="position:static">04</span></div>
    <p class="label" style="left:22px;top:80px;color:var(--sky)">Our Project</p>
    <p class="lorem" style="left:22px;top:85px;width:112px">Selected holdings and the results delivered for investors over recent years.</p>
    <div style="left:0;top:106px;width:14px;height:14px;border:1px solid #b6e8f1;border-radius:50%;font-size:3.6px;display:flex;align-items:center;justify-content:center;color:#b6e8f1"><span style="position:static">05</span></div>
    <p class="label" style="left:22px;top:106px;color:#b6e8f1">Contact Us</p>
    <p class="lorem" style="left:22px;top:111px;width:112px">Where to reach our investor relations team and our offices worldwide.</p>
  </div>
</section>

<section class="slide col3 row1">
  <h2 class="heading barred" style="left:20px;top:78px">Introducing</h2>
  <p class="lorem" style="left:26px;top:98px;width:92px">We partner with sophisticated investors to build resilient portfolios, combining careful research, patient capital and clear reporting across each stage of the investment cycle.</p>
  <p class="label" style="left:26px;top:132px;color:var(--ink)">John Doe</p>
  <p class="lorem" style="left:26px;top:137px;font-style:italic">The Fund Leader</p>
  <div class="art" role="img" aria-label="Illustration of an hourglass filled with coins" style="left:178px;top:43px;width:93px;height:135px"></div>
  <div class="art" role="img" aria-label="Illustration of a hand placing a coin beside a car" style="left:125px;top:97px;width:76px;height:76px;border-radius:50%;border:3px solid var(--white);background:linear-gradient(160deg,#aeb2ea,#7377c8)"></div>
</section>

<section class="slide col4 row1">
  <p class="vlabel" style="left:17px;top:64px;height:93px;text-align:center">Pangolin Capital Partners</p>
  <div class="art" role="img" aria-label="Illustration of a figure pointing toward a goal" style="left:27px;top:64px;width:84px;height:93px"></div>
  <h2 class="heading barred" style="left:125px;top:72px">About Company</h2>
  <p class="num" style="left:132px;top:93px;font-size:15px;color:var(--ink)">2020</p>
  <p class="lorem" style="left:170px;top:95px;width:92px">Founded to serve long term capital with a focused global mandate.</p>
  <p class="lorem" style="left:132px;top:109px;width:130px">Our investment committee reviews every opportunity against strict risk limits, sector outlooks and the interests of the partners who entrust us with their capital.</p>
  <p class="lorem" style="left:132px;top:138px;width:130px;font-style:italic;color:var(--navy);font-size:3.6px">However difficult the market may seem, there is always something you can do and succeed at.</p>
</section>

<!-- Row 2 -->
<section class="slide col1 row2">
  <div class="art" role="img" aria-label="Illustration of people assembling large letters" style="left:25px;top:43px;width:60px;height:60px"></div>
  <div class="art" role="img" aria-label="Illustration of a ladder against a large dollar sign" style="left:28px;top:117px;width:82px;height:61px"></div>
  <h2 class="heading barred" style="left:126px;top:69px">Pangolin Mission</h2>
  <p class="lorem" style="left:133px;top:88px;width:128px">We aim to grow investor capital responsibly, backing proven managers and businesses with strong governance and clear paths to value.</p>
  <p class="label bullet" style="left:134px;top:110px">Mission One</p>
  <p class="lorem" style="left:141px;top:116px;width:120px">Deliver consistent risk adjusted returns through every market cycle we face.</p>
  <p class="label bullet" style="left:134px;top:133px">Mission Two</p>
  <p class="lorem" style="left:141px;top:139px;width:120px">Report openly and promptly so investors always understand their exposure.</p>
</section>

<section class="slide col2 row2">
  <h2 class="heading barred" style="left:20px;top:69px">Company<br>Timeline</h2>
  <p class="lorem" style="left:26px;top:108px;width:72px">A short record of milestones that shaped the fund, from first close to our present global reach and growing investor base.</p>
  <p class="year" style="left:138px;top:73px">2016</p>
  <div class="art" role="img" aria-label="Illustration of a hand holding a pile of coins" style="left:112px;top:89px;width:72px;height:44px"></div>
  <p class="label" style="left:122px;top:139px">Description</p>
  <p class="lorem" style="left:122px;top:145px;width:58px">First fund closed with a small group of founding partners and a clear mandate.</p>
  <p class="year" style="left:224px;top:73px">2017</p>
  <div class="art" role="img" aria-label="Illustration of a payment card and a person" style="left:198px;top:89px;width:72px;height:44px"></div>
  <p class="label" style="left:208px;top:139px">Description</p>
  <p class="lorem" style="left:208px;top:145px;width:58px">Expanded the team and opened a second office to cover new regional markets.</p>
</section>

<section class="slide col3 row2">
  <p class="year" style="left:53px;top:58px">2018</p>
  <div class="art" role="img" aria-label="Illustration of a wallet with coins" style="left:26px;top:73px;width:72px;height:45px"></div>
  <p class="label" style="left:34px;top:124px">Description</p>
  <p class="lorem" style="left:34px;top:130px;width:58px">Launched a dedicated credit strategy for institutional investors.</p>
  <p class="year" style="left:139px;top:58px">2019</p>
  <div class="art" role="img" aria-label="Illustration of a coin jar and a person" style="left:112px;top:73px;width:72px;height:45px"></div>
  <p class="label" style="left:120px;top:124px">Description</p>
  <p class="lorem" style="left:120px;top:130px;width:58px">Passed a major milestone in assets under management worldwide.</p>
  <p class="year" style="left:225px;top:58px">2020</p>
  <div class="art" role="img" aria-label="Illustration of a person climbing a rising arrow" style="left:198px;top:73px;width:72px;height:45px"></div>
  <p class="label" style="left:206px;top:124px">Description</p>
  <p class="lorem" style="left:206px;top:130px;width:58px">Introduced a sustainable investing framework across all funds.</p>
</section>

<section class="slide col4 row2">
  <div class="photo-city" role="img" aria-label="Photograph of a city skyline with connection lines" style="left:15px;top:43px;width:101px;height:58px;clip-path:polygon(0 0,45% 25%,100% 0,100% 55%,55% 100%,0 55%)"></div>
  <div class="pill-v" style="left:138px;top:43px;height:96px"><span>Pangolin Capital Partners</span></div>
  <h2 class="heading barred" style="left:164px;top:76px">Company<br>Service</h2>
  <p class="label" style="left:170px;top:115px;font-size:4px">Service Description</p>
  <p class="lorem" style="left:170px;top:120px;width:95px">Advisory, fund management and co-investment for qualified investors seeking global diversification.</p>
  <p class="lorem" style="left:41px;top:108px;width:90px">Every mandate is built around the goals and risk appetite of our partners.</p>
  <p class="lorem bullet" style="left:43px;top:121px;width:92px">If a strategy stops working, we change course early.</p>
  <p class="lorem bullet" style="left:43px;top:129px;width:92px">Setbacks teach discipline, discipline builds returns.</p>
  <p class="lorem bullet" style="left:43px;top:137px;width:92px">Act on conviction and let results do the talking.</p>
  <p class="lorem bullet" style="left:43px;top:145px;width:92px">A clear goal is a plan with a firm deadline.</p>
  <p class="lorem bullet" style="left:43px;top:153px;width:92px">Our judgement is careful, precise and unique.</p>
</section>

<!-- Row 3 -->
<section class="slide col1 row3">
  <div role="img" aria-label="Photograph of a city skyline at night with network lines" style="left:14px;top:48px;width:257px;height:125px;background:linear-gradient(180deg,#1d3f86 0%,#142b63 50%,#0a1737 100%)"></div>
  <div style="left:26px;top:69px;width:1px;height:30px;background:var(--white)"></div>
  <h2 class="heading" style="left:34px;top:64px;font-size:18px;color:var(--white);line-height:1.4">Break<br>Section</h2>
  <p style="left:34px;top:117px;font-size:7px;color:var(--white)">12.05 pm – 12.45 pm</p>
  <p class="lorem" style="left:34px;top:130px;width:104px;color:#cdd6ea">A short pause before we move into the portfolio review, performance figures and the outlook for the year ahead.</p>
</section>

<section class="slide col2 row3">
  <div class="pill-h" style="left:34px;top:43px;width:95px">Pangolin Capital Partners</div>
  <div class="art" role="img" aria-label="Illustration of people collecting coins from a tree" style="left:14px;top:63px;width:64px;height:114px"></div>
  <div style="left:85px;top:63px;width:60px;height:57px;background:var(--navy);border:1.5px solid var(--white);outline:1px solid var(--navy)">
    <svg style="left:24px;top:5px" width="12" height="14" viewBox="0 0 12 14"><path d="M3 0 L6 5 L9 0" fill="none" stroke="#8fb4e8" stroke-width="1.5"/><circle cx="6" cy="9" r="4" fill="#8fb4e8"/></svg>
    <p style="left:7px;top:24px;font-size:23px;color:var(--white);line-height:1">99%</p>
  </div>
  <p style="left:100px;top:126px;font-size:13px;color:var(--navy)">+214</p>
  <p class="label" style="left:102px;top:144px">Description</p>
  <p class="lorem" style="left:92px;top:150px;width:50px;text-align:center">Portfolio companies backed since our first close.</p>
  <div style="left:160px;top:63px;width:1px;height:30px;background:var(--ink)"></div>
  <h2 class="heading" style="left:168px;top:64px">Pangolin<br>Portfolio</h2>
  <p class="label bullet" style="left:168px;top:109px">Portfolio One</p>
  <p class="lorem" style="left:175px;top:115px;width:95px">Growth equity positions in established businesses with strong cash flow.</p>
  <p class="label bullet" style="left:168px;top:140px">Portfolio Two</p>
  <p class="lorem" style="left:175px;top:146px;width:95px">Private credit facilities secured against high quality assets worldwide.</p>
</section>

<section class="slide col3 row3">
  <h2 class="heading barred" style="left:20px;top:71px">Our<br>Portfolio</h2>
  <p class="lorem" style="left:26px;top:110px;width:88px">Our holdings span private equity, credit and real assets, selected for resilience and long term value creation for investors.</p>
  <p class="lorem" style="left:154px;top:52px;font-weight:600;color:var(--navy)">Description One.</p>
  <p class="lorem" style="left:253px;top:52px;font-weight:600;color:var(--navy)">91%</p>
  <div style="left:154px;top:58px;width:107px;height:3px;border-radius:2px;background:var(--rule)"><div style="left:0;top:0;width:97px;height:3px;border-radius:2px;background:var(--navy)"></div></div>
  <p class="lorem" style="left:154px;top:68px;font-weight:600;color:var(--navy)">Description Two.</p>
  <p class="lorem" style="left:253px;top:68px;font-weight:600;color:var(--navy)">86%</p>
  <div style="left:154px;top:74px;width:107px;height:3px;border-radius:2px;background:var(--rule)"><div style="left:0;top:0;width:92px;height:3px;border-radius:2px;background:var(--navy)"></div></div>
  <div class="photo-light" role="img" aria-label="Photograph of office towers" style="left:127px;top:84px;width:70px;height:93px"></div>
  <svg style="left:127px;top:140px" width="56" height="37" viewBox="0 0 56 37"><polygon points="0,0 56,18 0,37" fill="#1b5fb5"/></svg>
  <div role="img" aria-label="Photograph of a laptop showing charts" style="left:200px;top:84px;width:70px;height:45px;background:linear-gradient(160deg,#c9d3e0,#5f7590)"></div>
  <div role="img" aria-label="Photograph of hands using a digital screen" style="left:200px;top:132px;width:70px;height:45px;background:linear-gradient(160deg,#4d8fd2,#1c3f7a)"></div>
</section>

<section class="slide col4 row3">
  <h2 class="heading barred" style="left:20px;top:50px">Our Latest Work</h2>
  <p class="lorem" style="left:33px;top:82px;width:100px">Recent transactions completed on behalf of our investors, from sourcing and diligence to a successful close.</p>
  <p class="label" style="left:33px;top:102px">Description</p>
  <p class="num" style="left:33px;top:107px">379K</p>
  <p class="lorem" style="left:77px;top:111px;width:55px">Capital deployed in the latest quarter.</p>
  <p class="label" style="left:33px;top:129px">Description</p>
  <p class="num" style="left:33px;top:134px">2.851</p>
  <p class="lorem" style="left:77px;top:138px;width:55px">Investor accounts served across regions.</p>
  <p class="lorem bullet" style="left:35px;top:155px;width:100px">Three new mandates closed this year.</p>
  <p class="lorem bullet" style="left:35px;top:163px;width:100px">Two successful exits delivered to partners.</p>
  <div class="photo-city" role="img" aria-label="Photograph of glass skyscrapers against the sky" style="left:150px;top:91px;width:101px;height:67px"></div>
  <div class="pill-v" style="left:256px;top:77px;height:94px"><span>Pangolin Capital Partners</span></div>
</section>

<!-- Row 4 -->
<section class="slide col1 row4">
  <div class="pill-v" style="left:15px;top:43px;height:94px"><span>Pangolin Capital Partners</span></div>
  <div style="left:48px;top:43px;width:57px;height:114px;border-radius:7px;background:#1a1a1a;padding:2px">
    <div class="art" role="img" aria-label="Illustration of a speaker at a podium on the phone screen" style="left:2.5px;top:2.5px;width:52px;height:109px;border-radius:5px"></div>
  </div>
  <p class="label" style="left:58px;top:162px;color:var(--ink)">Your Title Here</p>
  <div style="left:120px;top:69px;width:1px;height:30px;background:var(--ink)"></div>
  <h2 class="heading" style="left:127px;top:69px">Amazing Device<br>Mockup Slide</h2>
  <p class="lorem" style="left:127px;top:105px;width:125px">Present key figures and investor material on a mobile screen, keeping the story simple and the numbers easy to follow.</p>
  <div style="left:127px;top:136px;width:13px;height:13px;border-radius:50%;background:var(--navy)">
    <svg style="left:3.5px;top:3.5px" width="6" height="6" viewBox="0 0 6 6"><rect x="0.3" y="0.3" width="5.4" height="4" fill="none" stroke="#fff" stroke-width="0.7"/><path d="M3 4.3 V6" stroke="#fff" stroke-width="0.7"/></svg>
  </div>
  <p class="label" style="left:145px;top:136px">Mockup Description</p>
  <p class="lorem" style="left:145px;top:142px;width:105px">Swap the screen content for any chart or summary page.</p>
</section>

<section class="slide col2 row4">
  <p class="lorem" style="left:23px;top:57px;font-weight:600;color:var(--ink)">Download</p>
  <p class="num" style="left:23px;top:60px;color:var(--ink)">379K</p>
  <p class="lorem" style="left:66px;top:63px;width:62px">Reports downloaded by partners this year.</p>
  <div style="left:0;top:79px;width:117px;height:93px;background:#1a1a1a;border-radius:0 4px 4px 0">
    <div role="img" aria-label="Tablet screen showing a business investment webpage" style="left:0;top:5px;width:111px;height:83px;background:linear-gradient(120deg,#c63fb0,#7a3fd1 45%,#f4f1fb 46%)"></div>
  </div>
  <div class="pill-v" style="left:135px;top:52px;height:95px"><span>Pangolin Capital Partners</span></div>
  <h2 class="heading" style="left:170px;top:67px;line-height:1.3">Tablet<br>Mockup<br>Design</h2>
  <p class="lorem" style="left:170px;top:124px;width:88px">Use the tablet layout to show a dashboard, a fund summary or the investor portal at a glance.</p>
</section>

<section class="slide col3 row4">
  <h2 class="heading barred" style="left:20px;top:52px">Chart Slide</h2>
  <svg style="left:26px;top:72px" width="250" height="86" viewBox="0 0 250 86">
    <g font-family="Poppins" font-size="3" fill="#8a8f9c">
      <text x="0" y="2">160</text><text x="0" y="8.5">150</text><text x="0" y="15">140</text><text x="0" y="21.5">120</text><text x="0" y="28">100</text><text x="0" y="34.5">80</text><text x="0" y="41">60</text><text x="0" y="47.5">40</text><text x="0" y="54">20</text><text x="0" y="60.5">0</text>
      <text x="16" y="67">Jan</text><text x="35" y="67">Feb</text><text x="54" y="67">Mar</text><text x="73" y="67">Apr</text><text x="92" y="67">May</text><text x="111" y="67">Jun</text><text x="130" y="67">Jul</text><text x="148" y="67">Aug</text><text x="167" y="67">Sep</text><text x="186" y="67">Oct</text><text x="205" y="67">Nov</text><text x="224" y="67">Dec</text>
    </g>
    <g stroke="#eceef3" stroke-width="0.4"><line x1="10" y1="1" x2="236" y2="1"/><line x1="10" y1="14" x2="236" y2="14"/><line x1="10" y1="27" x2="236" y2="27"/><line x1="10" y1="40" x2="236" y2="40"/><line x1="10" y1="53" x2="236" y2="53"/><line x1="10" y1="60" x2="236" y2="60"/></g>
    <polyline points="18,59 37,58 56,56 75,52 94,46 113,37 132,26 151,20 170,17 189,20 208,31 227,39" fill="none" stroke="#1a2470" stroke-width="0.7"/>
    <polyline points="18,59 37,59 56,58 75,57 94,56 113,54 132,51 151,45 170,38 189,41 208,47 227,49" fill="none" stroke="#1a2470" stroke-width="0.7"/>
    <g fill="#1a2470"><circle cx="18" cy="59" r="0.9"/><circle cx="37" cy="58" r="0.9"/><circle cx="56" cy="56" r="0.9"/><circle cx="75" cy="52" r="0.9"/><circle cx="94" cy="46" r="0.9"/><circle cx="113" cy="37" r="0.9"/><circle cx="132" cy="26" r="0.9"/><circle cx="151" cy="20" r="0.9"/><circle cx="170" cy="17" r="0.9"/><circle cx="189" cy="20" r="0.9"/><circle cx="208" cy="31" r="0.9"/><circle cx="227" cy="39" r="0.9"/><circle cx="170" cy="38" r="0.9"/><circle cx="208" cy="47" r="0.9"/><circle cx="227" cy="49" r="0.9"/></g>
  </svg>
  <p class="lorem" style="left:26px;top:155px;width:110px">Monthly net asset value for the two core strategies, showing steady growth through the middle of the year.</p>
  <svg style="left:156px;top:155px" width="12" height="12" viewBox="0 0 12 12"><circle cx="6" cy="6" r="5" fill="none" stroke="#111318" stroke-width="0.8"/><path d="M6 1 V6 H11" fill="none" stroke="#111318" stroke-width="0.8"/></svg>
  <p class="label" style="left:173px;top:154px">Chart Description</p>
  <p class="lorem" style="left:173px;top:160px;width:85px">Values shown in millions, before fees and expenses.</p>
</section>

<section class="slide col4 row4">
  <svg style="left:20px;top:66px" width="150" height="86" viewBox="0 0 150 86">
    <g font-family="Poppins" font-size="3" fill="#8a8f9c"><text x="0" y="6">6</text><text x="0" y="18.5">5</text><text x="0" y="31">4</text><text x="0" y="43.5">3</text><text x="0" y="56">2</text><text x="0" y="68.5">1</text><text x="0" y="81">0</text><text x="18" y="88">Day 1</text><text x="52" y="88">Day 2</text><text x="86" y="88">Day 3</text><text x="119" y="88">Day 4</text></g>
    <g stroke="#eceef3" stroke-width="0.4"><line x1="6" y1="5" x2="142" y2="5"/><line x1="6" y1="17.5" x2="142" y2="17.5"/><line x1="6" y1="30" x2="142" y2="30"/><line x1="6" y1="42.5" x2="142" y2="42.5"/><line x1="6" y1="55" x2="142" y2="55"/><line x1="6" y1="67.5" x2="142" y2="67.5"/><line x1="6" y1="80" x2="142" y2="80"/></g>
    <rect x="55" y="20" width="68" height="35" fill="#121a61"/>
    <polyline points="22,55 55,55" fill="none" stroke="#1b5fb5" stroke-width="0.7"/>
    <polyline points="22,35 55,55" fill="none" stroke="#111318" stroke-width="0.6"/>
    <polyline points="22,55 55,20 88,55 123,15" fill="none" stroke="#1b5fb5" stroke-width="0.7"/>
    <rect x="12" y="27" width="16" height="10" rx="1.5" fill="#121a61"/><text x="15" y="34" font-family="Poppins" font-size="5" fill="#fff">2.0</text>
    <rect x="47" y="7" width="16" height="10" rx="1.5" fill="#121a61"/><text x="50" y="14" font-family="Poppins" font-size="5" fill="#fff">4.4</text>
    <rect x="115" y="2" width="16" height="10" rx="1.5" fill="#1b5fb5"/><text x="118" y="9" font-family="Poppins" font-size="5" fill="#fff">5.2</text>
  </svg>
  <h2 class="heading barred" style="left:170px;top:53px">Chart Slide</h2>
  <p class="lorem" style="left:177px;top:73px;width:95px">Daily flows across the reporting week, with the shaded band marking the target allocation range for the fund.</p>
  <p class="label bullet" style="left:177px;top:105px;color:var(--blue)">Chart One.</p>
  <p class="lorem" style="left:183px;top:111px;width:88px">Opening position recorded on day one.</p>
  <p class="label bullet" style="left:177px;top:128px;color:var(--blue)">Chart Two.</p>
  <p class="lorem" style="left:183px;top:134px;width:88px">Peak allocation reached mid week.</p>
  <p class="label bullet" style="left:177px;top:151px;color:var(--blue)">Chart Three.</p>
  <p class="lorem" style="left:183px;top:157px;width:88px">Closing value at the end of day four.</p>
</section>

<!-- Row 5 -->
<section class="slide col1 row5">
  <h2 class="heading barred" style="left:20px;top:51px">Our Creative Process</h2>
  <p class="lorem" style="left:26px;top:72px;width:232px">From first meeting to final report, each engagement follows a clear sequence so investors know what happens next and why it matters to their capital.</p>
  <div style="left:23px;top:98px;width:28px;height:28px;border-radius:50%;background:var(--navy)"><svg style="left:10px;top:8px" width="8" height="12" viewBox="0 0 8 12"><circle cx="4" cy="4" r="3.2" fill="none" stroke="#fff" stroke-width="0.8"/><path d="M2.8 8 H5.2 M3 9.8 H5" stroke="#fff" stroke-width="0.8"/></svg></div>
  <div style="left:93px;top:98px;width:28px;height:28px;border-radius:50%;background:var(--navy)"><svg style="left:9px;top:9px" width="10" height="10" viewBox="0 0 10 10"><circle cx="4" cy="4" r="3" fill="none" stroke="#fff" stroke-width="0.8"/><path d="M6.2 6.2 L9 9" stroke="#fff" stroke-width="0.9"/></svg></div>
  <div style="left:164px;top:98px;width:28px;height:28px;border-radius:50%;background:var(--blue)"><svg style="left:9px;top:9px" width="10" height="10" viewBox="0 0 10 10"><path d="M1 1 V9 H9" fill="none" stroke="#fff" stroke-width="0.8"/><path d="M2.5 7 L5 4.5 L6.5 6 L8.5 3" fill="none" stroke="#fff" stroke-width="0.8"/></svg></div>
  <div style="left:234px;top:98px;width:28px;height:28px;border-radius:50%;background:var(--sky)"><svg style="left:9px;top:9px" width="10" height="10" viewBox="0 0 10 10"><circle cx="5" cy="5.5" r="3.8" fill="none" stroke="#fff" stroke-width="0.8"/><path d="M5 3.5 V5.5 H6.5 M3.8 0.8 H6.2" fill="none" stroke="#fff" stroke-width="0.8"/></svg></div>
  <svg style="left:61px;top:118px" width="20" height="12" viewBox="0 0 20 12"><path d="M1 1 L10 10 L19 1" fill="none" stroke="#8fa8ee" stroke-width="2.2"/></svg>
  <svg style="left:132px;top:94px" width="20" height="12" viewBox="0 0 20 12"><path d="M1 11 L10 2 L19 11" fill="none" stroke="#8fa8ee" stroke-width="2.2"/></svg>
  <svg style="left:203px;top:118px" width="20" height="12" viewBox="0 0 20 12"><path d="M1 1 L10 10 L19 1" fill="none" stroke="#8fd6ee" stroke-width="2.2"/></svg>
  <p class="label" style="left:21px;top:143px;color:var(--ink)">Description</p>
  <p class="lorem" style="left:10px;top:149px;width:54px;text-align:center">Define goals and the investor profile.</p>
  <p class="label" style="left:91px;top:143px;color:var(--ink)">Description</p>
  <p class="lorem" style="left:80px;top:149px;width:54px;text-align:center">Research and screen each opportunity.</p>
  <p class="label" style="left:162px;top:143px;color:var(--navy)">Description</p>
  <p class="lorem" style="left:151px;top:149px;width:54px;text-align:center">Build and test the target portfolio.</p>
  <p class="label" style="left:232px;top:143px;color:var(--blue)">Description</p>
  <p class="lorem" style="left:221px;top:149px;width:54px;text-align:center">Monitor and report on a set schedule.</p>
</section>

<section class="slide col2 row5">
  <div role="img" aria-label="World map of investor regions" style="left:146px;top:52px;width:130px;height:115px;border-radius:40% 50% 45% 55%;background:linear-gradient(160deg,#eef0f5,#dde1ea)"></div>
  <h2 class="heading barred" style="left:18px;top:81px;font-size:13px">Demographics</h2>
  <p class="lorem" style="left:25px;top:102px;width:88px">Our investor base by region, showing where the majority of committed capital comes from today.</p>
  <div style="left:204px;top:74px;width:33px;height:33px;border-radius:50%;background:var(--blue);border:2px solid var(--white)">
    <p style="left:0;top:8px;width:29px;text-align:center;font-size:5px;color:var(--white)">19%</p>
    <p style="left:0;top:16px;width:29px;text-align:center;font-size:2.6px;color:var(--white);font-weight:600">Remarks</p>
  </div>
  <div style="left:153px;top:100px;width:29px;height:29px;border-radius:50%;background:#141823">
    <p style="left:0;top:8px;width:29px;text-align:center;font-size:5px;color:var(--white)">39%</p>
    <p style="left:0;top:15px;width:29px;text-align:center;font-size:2.6px;color:var(--white);font-weight:600">Remarks</p>
  </div>
  <div style="left:195px;top:127px;width:34px;height:34px;border-radius:50%;background:var(--navy)">
    <p style="left:0;top:11px;width:34px;text-align:center;font-size:5px;color:var(--white)">42%</p>
    <p style="left:0;top:18px;width:34px;text-align:center;font-size:2.6px;color:var(--white);font-weight:600">Remarks</p>
  </div>
</section>

<section class="slide col3 row5">
  <h2 class="heading barred" style="left:20px;top:58px">Stay Connected<br>With Us</h2>
  <p class="lorem" style="left:26px;top:95px;width:110px">Our investor relations team is available to answer questions, arrange meetings and share the latest fund reports.</p>
  <div style="left:29px;top:122px;width:20px;height:47px;border:1px solid var(--ink)">
    <p style="left:2px;top:3px;writing-mode:vertical-rl;transform:rotate(180deg);font-size:12px;color:var(--ink)">2020</p>
  </div>
  <svg style="left:70px;top:128px" width="5" height="4" viewBox="0 0 5 4"><rect x="0.2" y="0.2" width="4.6" height="3.6" fill="none" stroke="#111318" stroke-width="0.4"/><path d="M0.2 0.2 L2.5 2 L4.8 0.2" fill="none" stroke="#111318" stroke-width="0.4"/></svg>
  <p class="label" style="left:79px;top:126px">Email</p>
  <p class="lorem" style="left:79px;top:132px">hello@pangolincap.com</p>
  <svg style="left:70px;top:147px" width="5" height="5" viewBox="0 0 5 5"><path d="M0.3 4.7 V2 L2.5 0.3 L4.7 2 V4.7 Z" fill="none" stroke="#111318" stroke-width="0.4"/></svg>
  <p class="label" style="left:79px;top:145px">Locations</p>
  <p class="lorem" style="left:79px;top:151px">12 Harbour Row<br>London, United Kingdom</p>
  <div role="img" aria-label="Photograph of team members stacking hands" style="left:150px;top:59px;width:114px;height:91px;background:linear-gradient(160deg,#e9ecf1,#9aa3b3)"></div>
  <div class="pill-h" style="left:158px;top:144px;width:95px">Pangolin Capital Partners</div>
</section>

<section class="slide col4 row5">
  <div role="img" aria-label="Photograph of a city skyline with network lines" style="left:14px;top:56px;width:256px;height:57px;background:linear-gradient(180deg,#3a7fd0 0%,#1d4f9e 55%,#0c2456 100%)"></div>
  <div style="left:128px;top:121px;width:30px;height:1px;background:var(--ink)"></div>
  <h2 class="heading" style="left:0;top:129px;width:285px;text-align:center;font-size:16px">See You Next Time</h2>
  <p class="lorem" style="left:46px;top:152px;width:193px;text-align:center">Thank you for your time. We look forward to building lasting value together, one careful decision at a time, with partners who share our view.</p>
</section>

</body>
</html>
```